Duel Business card

Want an edgy business card that shows both of our companies on each side of the card, OR both together with a cool design.

*Must be edgy: We have attached our two business logos. We are a bail bond and immigration bond company.

Would like the address on one side only.
Need Phone, cell, website, address, and Name

Company Name 1: Liberty Release Partners
www.libertyreleasepartners-example.com

Company Name 2: Crossway Custody Advocates
www.crosswaycustodyadvocates-example.com

These cards will need to be easily changeable so I can modify new employees

Target Market(s)

people in jail, takign imigrants out of jail and from being taken back to there country

Industry/Entity Type

Business

Requirements
Must have
• Include both logos attached

```html
<!DOCTYPE html>
<html lang="en">
<head>
<meta charset="utf-8">
<title>Liberty Release Partners &amp; Crossway Custody Advocates – Business Card</title>
<link rel="stylesheet" href="https://fonts.googleapis.com/css2?family=Lato:wght@400;700;900&display=swap">
<style>
  :root {
    --navy: #1e3a8f;
    --gold: #dfb61c;
    --red: #d2181d;
    --ink: #222428;
    --card: #fbfbfa;
    --backdrop: #e7e5e1;
  }
  * { box-sizing: border-box; margin: 0; padding: 0; }
  html, body { width: 1200px; height: 720px; overflow: hidden; }
  body {
    background: var(--backdrop);
    font-family: "Lato", sans-serif;
    color: var(--ink);
    position: relative;
  }
  .card {
    position: absolute;
    top: 205px;
    width: 540px;
    height: 310px;
    background: var(--card);
    box-shadow: 0 6px 18px rgba(0,0,0,.18);
    overflow: hidden;
  }
  .card--front { left: 40px; }
  .card--back { left: 620px; }

  .brand { position: absolute; display: flex; align-items: center; gap: 10px; }
  .brand__dot { flex: none; border-radius: 50%; }
  .brand__name { font-weight: 900; line-height: 1.05; text-transform: uppercase; letter-spacing: .5px; }
  .brand--bail .brand__dot { background: var(--navy); }
  .brand--bail .brand__name { color: var(--navy); }
  .brand--immigration .brand__dot { border: 3px solid var(--red); background: transparent; }
  .brand--immigration .brand__name { color: var(--red); }

  /* Front */
  .card--front .brand--bail { left: 96px; top: 52px; }
  .card--front .brand--bail .brand__dot { width: 34px; height: 34px; }
  .card--front .brand--bail .brand__name { font-size: 15px; }
  .card--front .brand--immigration { left: 330px; top: 44px; }
  .card--front .brand--immigration .brand__dot { width: 50px; height: 50px; }
  .card--front .brand--immigration .brand__name { font-size: 12px; }

  .rule { position: absolute; left: 70px; right: 70px; height: 1.5px; background: var(--navy); }
  .rule--top { top: 132px; }
  .rule--bottom { top: 190px; }

  .person { position: absolute; top: 142px; left: 0; right: 0; text-align: center; font-size: 26px; font-weight: 400; }

  .contact { position: absolute; left: 0; right: 0; top: 202px; display: flex; flex-direction: column; align-items: center; gap: 9px; font-size: 15px; }
  .contact__row { display: flex; gap: 22px; align-items: center; }
  .contact__item { display: flex; align-items: center; gap: 7px; white-space: nowrap; }
  .contact__icon { width: 13px; height: 13px; fill: var(--navy); flex: none; }

  /* Back */
  .card--back .brand--bail { left: 48px; top: 100px; }
  .card--back .brand--bail .brand__dot { width: 46px; height: 46px; }
  .card--back .brand--bail .brand__name { font-size: 20px; }
  .card--back .brand--immigration { left: 330px; top: 44px; }
  .card--back .brand--immigration .brand__dot { width: 62px; height: 62px; }
  .card--back .brand--immigration .brand__name { font-size: 13px; }

  .web-bands { position: absolute; left: 0; right: 0; top: 212px; height: 36px; display: flex; }
  .web-band { flex: 1; display: flex; align-items: center; justify-content: center; color: #fff; font-size: 12px; white-space: nowrap; }
  .web-band--bail { background: var(--gold); }
  .web-band--immigration { background: var(--red); }
</style>
</head>
<body>

<section class="card card--front" aria-label="Card front">
  <div class="brand brand--bail">
    <span class="brand__dot"></span>
    <span class="brand__name">Liberty Release<br>Partners</span>
  </div>
  <div class="brand brand--immigration">
    <span class="brand__dot"></span>
    <span class="brand__name">Crossway Custody<br>Advocates</span>
  </div>

  <div class="rule rule--top"></div>
  <h1 class="person">Sam Rivera</h1>
  <div class="rule rule--bottom"></div>

  <div class="contact">
    <div class="contact__row">
      <span class="contact__item">
        <svg class="contact__icon" viewBox="0 0 16 16" aria-hidden="true"><path d="M2 3h3v10H2zM6 2h8v12H6zm2 2v3h4V4zm0 5v1h1V9zm2 0v1h1V9zm2 0v1h1V9zm-4 2v1h1v-1zm2 0v1h1v-1zm2 0v1h1v-1z"/></svg>
        0100 555 0142 ext 2201
      </span>
      <span class="contact__item">
        <svg class="contact__icon" viewBox="0 0 16 16" aria-hidden="true"><path d="M4 1h8a1 1 0 0 1 1 1v12a1 1 0 0 1-1 1H4a1 1 0 0 1-1-1V2a1 1 0 0 1 1-1zm1 2v8h6V3zm3 9a1 1 0 1 0 0 2 1 1 0 0 0 0-2z"/></svg>
        sam.rivera@example.com
      </span>
    </div>
    <div class="contact__row">
      <span class="contact__item">
        <svg class="contact__icon" viewBox="0 0 16 16" aria-hidden="true"><path d="M8 1 1 7.5h2V15h4v-4h2v4h4V7.5h2z"/></svg>
        Suite 4, Harbor Row, Northfield, NR2 7QT
      </span>
    </div>
  </div>
</section>

<section class="card card--back" aria-label="Card back">
  <div class="brand brand--bail">
    <span class="brand__dot"></span>
    <span class="brand__name">Liberty Release<br>Partners</span>
  </div>
  <div class="brand brand--immigration">
    <span class="brand__dot"></span>
    <span class="brand__name">Crossway Custody<br>Advocates</span>
  </div>

  <div class="web-bands">
    <span class="web-band web-band--bail">www.libertyreleasepartners-example.com</span>
    <span class="web-band web-band--immigration">www.crosswaycustodyadvocates-example.com</span>
  </div>
</section>

</body>
</html>
```